female esthetician looking for an impact business card

I an an expert in skin care industry with high experience in NYC.I want my business card to look professional , an impact at first look. I do want a combination between white and gold . I believe the font will be great if is gold.. The Fonts are also important. MIRELA COSTANDI (SKIN CARE BOUTIQUE)

THIS SHOULD BE THE BUSINESS NAME, and should be placed on th eback of the card.
IN front m, the name MIRELA COSTANDI - ESTHETCIAN

BY APPOINTMENTS ONLY: 512.478.2936

Target Market(s)

HIGH END CLIENTELE

Contact Information for Business Card

iT WILL BE on a luxury paper. I neeed the wow feeling

Requirements
Should not have
• pictures

```html
<!DOCTYPE html>
<html lang="en">
<head>
<meta charset="utf-8">
<title>Mirela Costandi – Business Card</title>
<link rel="stylesheet" href="https://fonts.googleapis.com/css2?family=Didact+Gothic&family=Arimo:ital,wght@0,400;0,700;1,400&display=swap">
<style>
  :root {
    --bg: #d6d6d6;
    --paper: #ffffff;
    --gold: #b8862b;
    --ink: #2b2b2b;
    --edge: #c9c9c9;
  }
  * { box-sizing: border-box; margin: 0; padding: 0; }
  html, body { width: 1200px; height: 915px; overflow: hidden; }
  body {
    background: var(--bg);
    font-family: "Arimo", Arial, sans-serif;
    color: var(--ink);
  }
  .canvas {
    position: relative;
    width: 1200px;
    height: 915px;
    display: flex;
    align-items: center;
    justify-content: center;
    gap: 60px;
  }
  .card {
    position: relative;
    width: 510px;
    height: 292px;
    background: var(--paper);
    box-shadow: 0 1px 0 var(--edge), 0 12px 30px rgba(0,0,0,0.12);
  }
  .brand {
    position: absolute;
    left: 50%;
    top: 50%;
    transform: translate(-50%, -50%);
    display: flex;
    align-items: center;
    gap: 14px;
  }
  .brand-dot {
    width: 34px;
    height: 34px;
    border-radius: 50%;
    background: var(--gold);
    flex: none;
  }
  .brand-text { display: flex; flex-direction: column; }
  .brand-name {
    font-family: "Didact Gothic", "Century Gothic", sans-serif;
    font-size: 34px;
    color: var(--gold);
    line-height: 1;
    white-space: nowrap;
  }
  .brand-tag {
    font-family: "Arimo", Arial, sans-serif;
    font-size: 9px;
    letter-spacing: 3px;
    color: var(--ink);
    text-align: right;
    margin-top: 6px;
    white-space: nowrap;
  }
  /* front card: smaller mark, set left of centre to leave room for the website */
  .brand--front {
    left: 96px;
    top: 138px;
    transform: translateY(-50%);
    gap: 12px;
  }
  .brand--front .brand-dot { width: 28px; height: 28px; }
  .brand--front .brand-name { font-size: 27px; }
  .brand--front .brand-tag { font-size: 8px; letter-spacing: 2.6px; margin-top: 5px; }

  .front-id {
    position: absolute;
    left: 26px;
    top: 22px;
  }
  .front-id .name {
    font-weight: 700;
    font-size: 12px;
    letter-spacing: 0.5px;
    color: var(--gold);
  }
  .front-id .title {
    font-style: italic;
    font-size: 10px;
    color: var(--ink);
    margin-top: 2px;
  }
  .contact {
    position: absolute;
    left: 26px;
    top: 176px;
    list-style: none;
    font-size: 11px;
  }
  .contact li { display: flex; align-items: center; gap: 7px; margin-top: 5px; }
  .contact svg { width: 13px; height: 13px; flex: none; }
  .website {
    position: absolute;
    right: 26px;
    top: 118px;
    font-size: 10.5px;
    letter-spacing: 0.5px;
    white-space: nowrap;
  }
  .address {
    position: absolute;
    right: 26px;
    bottom: 22px;
    font-size: 12px;
    line-height: 1.45;
    text-align: right;
  }
</style>
</head>
<body>
<main class="canvas">

  <section class="card card-front" aria-label="Card front">
    <div class="front-id">
      <p class="name">MIRELA COSTANDI</p>
      <p class="title">skin care expert</p>
    </div>

    <div class="brand brand--front">
      <span class="brand-dot"></span>
      <div class="brand-text">
        <span class="brand-name">Mirela Costandi</span>
        <span class="brand-tag">SKIN CARE EXPERT</span>
      </div>
    </div>

    <ul class="contact">
      <li>
        <svg viewBox="0 0 16 16" aria-hidden="true">
          <circle cx="8" cy="8" r="8" fill="#b8862b"/>
          <path d="M5.2 4.2l1.4-.2.8 1.9-.9.7c.4.9 1.1 1.6 2 2l.7-.9 1.9.8-.2 1.4c-3.3.2-5.9-2.4-5.7-5.7z" fill="#fff"/>
        </svg>
        <span>512.478.2936</span>
      </li>
      <li>
        <svg viewBox="0 0 16 16" aria-hidden="true">
          <circle cx="8" cy="8" r="8" fill="#b8862b"/>
          <rect x="4" y="5" width="8" height="6" fill="none" stroke="#fff" stroke-width="1"/>
          <path d="M4 5l4 3.4L12 5" fill="none" stroke="#fff" stroke-width="1"/>
        </svg>
        <span>info@costandiskin.com</span>
      </li>
    </ul>

    <p class="website">www.costandiskin.com</p>

    <p class="address">218 Linden Avenue, Suite 4<br>Brooklyn, NY 11201</p>
  </section>

  <section class="card card-back" aria-label="Card back">
    <div class="brand">
      <span class="brand-dot"></span>
      <div class="brand-text">
        <span class="brand-name">Mirela Costandi</span>
        <span class="brand-tag">SKIN CARE EXPERT</span>
      </div>
    </div>
  </section>

</main>
</body>
</html>
```